Launching a consulting business

I need a business card to launch a new consulting business. I provide executive level consultation throughout New York state to CEO and ED's who run and manage non-fo-profit corporations who support individuals with intellectual and developmental disabilities. The field is undergoing an evolution from a social model of care to more outcome based strategies. Having expertise in health care, leading a $50M business providing this service and working in the government creating policy I can bring to the Executive and corporations compassion, vision, strategy with a clear understanding of business practices for success. The field is moving to managed care. My background in health care management brings the expertise to create opportunities and possibilities. I currently have three projects I am consulting on - 1. Field expert assisting an accounting firm in the creation of a managed care application to become a managed care company supporting the ID/DD field. I crafted the care management model 2. Strategizing on product line creation to assure an agency is ready with a compendium services supporting the ID/DD field. 3. Facilitating a financial model to assist in predicting costs to render services in ID/DD. Developing and overlaying outcome measures to position agencies for effective marketing.
Quality is my passion and assuring all people live their life's dreams.
I would also like a template for letterhead stationary following what is created with my business card.
I wold like to incorporate a cranberry/sage tartan plaid within the design.

Please note my last name is spelled wrong on the attachment. I also do not want the tartan plaid used covering the entire card. i open to other ideas and suggestions.

Industry/Entity Type

Government

Contact Information for Business Card

Donna M Farris
Phone - 845-620-4178
Cell phone 845-733-2906
Email address - donnamfar@quillmail.com

```html
<!DOCTYPE html>
<html lang="en">
<head>
<meta charset="utf-8">
<title>Donna M Farris – Business Card</title>
<link rel="stylesheet" href="https://fonts.googleapis.com/css2?family=Cormorant+Garamond:wght@500&family=Didact+Gothic&display=swap">
<style>
  :root {
    --backdrop: #e9e7e3;
    --forest-deep: #0b2622;
    --forest-mid: #1c5549;
    --teal: #0f5f56;
    --teal-deep: #0a4640;
    --teal-edge: #0c4d46;
    --paper: #ffffff;
    --ink-light: #eef0ea;
    --ink-soft: #cfe0dc;
  }
  * { margin: 0; padding: 0; box-sizing: border-box; }
  html, body {
    width: 1200px; height: 871px; overflow: hidden;
    background: var(--backdrop);
  }
  .stage { position: relative; width: 1200px; height: 871px; }
  .card {
    position: absolute;
    width: 540px; height: 309px;
    border-radius: 4px;
    box-shadow: 0 10px 28px rgba(0,0,0,0.22);
    overflow: hidden;
  }
  .card-front {
    left: 70px; top: 120px;
    background: radial-gradient(ellipse 70% 65% at 52% 42%, var(--forest-mid) 0%, #134238 45%, var(--forest-deep) 100%);
  }
  .front-identity {
    position: absolute; left: 0; right: 0; top: 112px;
    text-align: center; color: var(--ink-light);
  }
  .name {
    font-family: "Cormorant Garamond", "Times New Roman", serif;
    font-weight: 500; letter-spacing: 0.5px;
  }
  .title {
    font-family: "Didact Gothic", "Century Gothic", sans-serif;
    letter-spacing: 0.6px;
  }
  .front-identity .name { font-size: 42px; line-height: 1; }
  .front-identity .title { font-size: 11px; margin-top: 6px; margin-left: 40px; color: var(--ink-soft); }

  .card-back {
    left: 590px; top: 440px;
    background: linear-gradient(100deg, var(--paper) 60%, #eeeeee 100%);
  }
  .back-band {
    position: absolute; left: 0; right: 0; top: 44px; height: 220px;
    background: linear-gradient(110deg, var(--teal) 0%, var(--teal-deep) 100%);
    border-top: 5px solid var(--teal-edge);
    border-bottom: 5px solid var(--teal-edge);
  }
  .back-identity { position: absolute; left: 34px; top: 20px; color: var(--ink-light); }
  .back-identity .name { font-size: 30px; line-height: 1; }
  .back-identity .title { font-size: 12.5px; margin-top: 4px; color: var(--ink-soft); }
  .contact-list {
    position: absolute; left: 260px; right: 24px; top: 118px;
    list-style: none;
    font-family: "Didact Gothic", "Century Gothic", sans-serif;
    font-size: 14px; letter-spacing: 0.8px; color: var(--ink-soft);
    white-space: nowrap;
  }
  .contact-list li { display: flex; align-items: center; height: 25px; }
  .contact-list svg { width: 16px; height: 16px; margin-right: 16px; flex: none; }
</style>
</head>
<body>
<main class="stage">
  <section class="card card-front">
    <div class="front-identity">
      <h1 class="name">Donna M Farris</h1>
      <p class="title">Executive Business Strategy Consultant</p>
    </div>
  </section>

  <section class="card card-back">
    <div class="back-band">
      <div class="back-identity">
        <h2 class="name">Donna M Farris</h2>
        <p class="title">Executive Business Strategy Consultant</p>
      </div>
      <ul class="contact-list">
        <li>
          <svg viewBox="0 0 16 16" fill="none" stroke="currentColor" stroke-width="1.2"><rect x="4.5" y="1" width="7" height="14" rx="1.2"/><line x1="7" y1="12.8" x2="9" y2="12.8"/></svg>
          845-733-2906
        </li>
        <li>
          <svg viewBox="0 0 16 16" fill="none" stroke="currentColor" stroke-width="1.2"><path d="M1.5 6.5c0-2 3-3.5 6.5-3.5s6.5 1.5 6.5 3.5l-2.5 1-1-2h-6l-1 2z"/><rect x="3" y="9" width="10" height="5.5" rx="1"/><circle cx="8" cy="11.7" r="1.3"/></svg>
          845-620-4178
        </li>
        <li>
          <svg viewBox="0 0 16 16" fill="none" stroke="currentColor" stroke-width="1.2"><rect x="1" y="3" width="14" height="10" rx="0.8"/><polyline points="1,3.5 8,9 15,3.5"/></svg>
          donnamfar@quillmail.com
        </li>
      </ul>
    </div>
  </section>
</main>
</body>
</html>
```